Internet Flyer for Voip and Fast Internet

I need a 2 sided A5 flyer for a bespoke service to residential flats...

Needs to stand out after dropping through the door...!

Target Market(s)

Central City Flats - High value occupants.

Industry/Entity Type

Residential

```html
<!DOCTYPE html>
<html lang="en">
<head>
<meta charset="utf-8">
<title>Halcyon Networks – Flyer</title>
<link rel="stylesheet" href="https://fonts.googleapis.com/css2?family=Open+Sans:wght@400;700&family=Carlito:wght@400;700&family=Cinzel:wght@900&display=swap">
<style>
:root{
  --ink:#1d1d1d;
  --ink-deep:#141414;
  --sheen:#cfcfcf;
  --white:#ffffff;
  --soft:#d8d8d8;
  --muted:#9a9a9a;
  --green:#8dbd3a;
  --red:#a11414;
  --red-deep:#5c0606;
  --rule:#5a5a5a;
  --sea:#1d5fc0;
}
*{margin:0;padding:0;box-sizing:border-box}
html,body{width:846px;height:1200px;overflow:hidden;background:#fff}
body{position:relative;font-family:"Carlito",Calibri,sans-serif;color:var(--white)}
.side{position:absolute;left:0;width:846px;background:var(--ink);overflow:hidden}
.side--front{top:0;height:598px}
.side--back{top:601px;height:599px}
.sheen{position:absolute;inset:0;width:100%;height:100%}
.abs{position:absolute}
.brand{left:22px;top:14px;font-family:"Open Sans",sans-serif;font-size:44px;font-weight:400;letter-spacing:.5px}
.tagline{left:22px;top:74px;font-family:"Open Sans",sans-serif;font-size:29px;color:var(--green)}
.pitch{left:607px;top:76px;width:170px;font-size:16px;line-height:24px}
.thumb{left:786px;top:80px;width:54px;height:74px;border-radius:14px;background:linear-gradient(160deg,#f2f2f2,#9c9c9c)}
.headline{left:23px;top:158px;font-family:"Cinzel",serif;font-weight:900;font-size:18px;color:#c9c9c9;letter-spacing:.4px;text-shadow:1px 1px 0 #000,-1px -1px 0 #555}
.lead{left:25px;top:205px;font-size:12px}
.lead--try{left:207px;top:229px}
.grid-v{left:333px;top:250px;height:205px;border-left:1px dashed var(--rule)}
.grid-h{left:10px;top:353px;width:645px;border-top:1px dashed var(--rule)}
.cell-title{font-size:10px;font-weight:700;color:var(--green)}
.cell-list{font-size:9.5px;line-height:12px;list-style:none}
.cell-list .status{color:var(--green)}
.cell-list li.item{padding-left:10px;position:relative}
.cell-list li.item::before{content:"";position:absolute;left:0;top:4px;width:4px;height:4px;background:var(--red)}
.pic{background:radial-gradient(circle at 40% 35%,var(--red),var(--red-deep))}
.callout{left:25px;top:497px;font-family:"Open Sans",sans-serif;font-weight:700;font-size:10.5px;line-height:26px;color:#e4e4e4;text-shadow:1px 1px 1px #000,0 0 2px #000}
.map{left:580px;top:435px;width:250px;height:124px;border-radius:40% 30% 45% 35%;background:radial-gradient(ellipse at 60% 45%,#4ea3f0,var(--sea) 65%,#0e3478)}
.url{left:543px;font-family:"Open Sans",sans-serif;font-weight:700;font-size:16.5px;text-shadow:1px 1px 2px #000}
.url--front{top:561px}
.url--back{top:557px}
.back-head{left:20px;top:16px;width:810px;font-family:"Open Sans",sans-serif;font-weight:700;font-size:15.5px;line-height:22px;color:#a8a8a8;text-shadow:1px 1px 1px #000}
.benefits{left:25px;top:75px;width:680px;list-style:none;font-size:13.6px;line-height:18.5px}
.benefits li{margin-bottom:12.5px}
.benefits li.highlight{color:var(--green)}
.dish-back{left:762px;top:472px;width:42px;height:44px}
</style>
</head>
<body>

<section class="side side--front">
  <svg class="sheen" viewBox="0 0 846 598" aria-hidden="true">
    <defs><linearGradient id="frontSheen" x1="1" y1="1" x2="0.5" y2="0.3">
      <stop offset="0" stop-color="#d8d8d8"/><stop offset="0.55" stop-color="#7a7a7a"/><stop offset="1" stop-color="#1d1d1d"/>
    </linearGradient></defs>
    <polygon points="846,130 846,598 330,598" fill="url(#frontSheen)"/>
  </svg>

  <h1 class="abs brand">Halcyon Networks</h1>
  <p class="abs tagline">Online solutions for your business</p>
  <p class="abs pitch">More than just your average hosting service; We bring all elements of online business under one roof.</p>
  <div class="abs thumb" role="img" aria-label="Hand giving a thumbs-up"></div>

  <h2 class="abs headline">MAKING AN EVEN BETTER INVESTMENT!</h2>
  <p class="abs lead">Are you fed up with slow internet and expensive phone calls?</p>
  <p class="abs lead lead--try">Try our “Four Play”………</p>

  <div class="abs grid-v"></div>
  <div class="abs grid-h"></div>

  <h3 class="abs cell-title" style="left:25px;top:279px">Phone Packages</h3>
  <svg class="abs" style="left:46px;top:296px" width="56" height="44" viewBox="0 0 56 44" aria-hidden="true">
    <path d="M4 14 C4 4 52 4 52 14 L52 19 L41 19 L41 13 C34 10 22 10 15 13 L15 19 L4 19 Z" fill="var(--red)"/>
    <path d="M14 20 L42 20 L50 42 L6 42 Z" fill="var(--red-deep)"/>
    <circle cx="28" cy="31" r="7" fill="none" stroke="var(--red)" stroke-width="3"/>
  </svg>
  <ul class="abs cell-list" style="left:170px;top:279px">
    <li class="status">Available Now</li>
    <li class="item">Line Rental only £4.99 per month</li>
    <li class="item">Cheap Calls to the world – eg USA<br>-1p per min, China 2p per min</li>
    <li class="item">Free Calls to the same network</li>
  </ul>

  <h3 class="abs cell-title" style="left:341px;top:279px">Internet Packages</h3>
  <div class="abs pic" style="left:374px;top:293px;width:28px;height:50px;border-radius:14px 14px 4px 4px" role="img" aria-label="Figure of a person online"></div>
  <ul class="abs cell-list" style="left:445px;top:279px">
    <li class="status">Sign Up Now</li>
    <li class="item">100Mbs up and down - £249 install &amp;</li>
    <li class="item">£99.00 per month Faster Speeds are</li>
    <li class="item">Available – up to 1 Gbs</li>
  </ul>

  <h3 class="abs cell-title" style="left:25px;top:368px">TV and HiFi over the Internet</h3>
  <div class="abs pic" style="left:54px;top:384px;width:52px;height:54px;border-radius:4px" role="img" aria-label="Television set"></div>
  <ul class="abs cell-list" style="left:170px;top:368px">
    <li class="status">Tell us what services you need</li>
    <li class="item">Aurel – Tunebay, Melodia etc</li>
    <li class="item">Lumatek</li>
    <li class="item">iPTV</li>
  </ul>

  <h3 class="abs cell-title" style="left:341px;top:368px">Corvia Telepresence</h3>
  <div class="abs pic" style="left:370px;top:390px;width:44px;height:47px;border-radius:50% 50% 4px 4px" role="img" aria-label="Satellite dish"></div>
  <p class="abs cell-list" style="left:445px;top:368px"><span class="status">Contact us for further information</span></p>

  <p class="abs callout">Remember the TV Program Zero Hour? Do you need to connect with people? We are able to connect<br>you to the video world to give you High Definition 50" + Video Calls and Conferencing……</p>

  <div class="abs map" role="img" aria-label="World map with network connection points"></div>
  <p class="abs url url--front">http://www.halcyon-networks.net</p>
</section>

<section class="side side--back">
  <svg class="sheen" viewBox="0 0 846 599" aria-hidden="true">
    <defs><linearGradient id="backSheen" x1="0" y1="0" x2="0.45" y2="0.55">
      <stop offset="0" stop-color="#bdbdbd"/><stop offset="0.6" stop-color="#4a4a4a"/><stop offset="1" stop-color="#1d1d1d"/>
    </linearGradient></defs>
    <polygon points="0,0 570,0 0,410" fill="url(#backSheen)"/>
  </svg>

  <h2 class="abs back-head">So here is my personal shortlist of the benefits of bandwidth, in an attempt to head off at least some of the folks who keep asking me that same dumb question:</h2>

  <ol class="abs benefits">
    <li>1.&nbsp; Delay kills all forms of human interaction and creativity. Less delay results in more effective interaction, innovation and output, and the relationship is highly non-linear so less delay translates into far more output.</li>
    <li>2.&nbsp; Ubiquitous (and symmetrical) videoconferencing that actually works can dramatically reduce our need to travel.</li>
    <li>3.&nbsp; Real-time (multi-user) collaborative environments can further accelerate (global) creativity and productivity by making virtual teaming a working reality.</li>
    <li>4.&nbsp; Imagine instantaneous access to information sources and resources of all kinds of forms and formats - uploads and downloads.</li>
    <li>5.&nbsp; Cloud computing with all applications and data online would dramatically reduce hardware and software costs, improve security markedly, and spawn new communities, business opportunities and industries.</li>
    <li>6.&nbsp; Virtual and augmented reality would come alive and change absolutely everything from working to entertainment, education, training and healthcare - and we can't even hazard a guess at the scale of improvement to be had.</li>
    <li>7.&nbsp; All forms of modelling and prediction - scientific, industrial, social and so on would be revolutionised by instant access to distributed resources worldwide.</li>
    <li>8.&nbsp; 3D prototyping and distributed production would become real and a part of the mainstream, and ultimately the new mainstream industry.</li>
    <li>9.&nbsp; Real-time access to global radio, TV, movies and other forms of entertainment at our convenience.</li>
    <li class="highlight">10.&nbsp; Vast tracts of radio spectrum for high-speed wireless apps would become available as services delivered by 'by fibre' reduce the need for services 'by radio'</li>
  </ol>

  <div class="abs dish-back" role="img" aria-label="Satellite dish" style="background:linear-gradient(160deg,#8a8a8a,#2e2e2e);border-radius:50% 50% 4px 4px"></div>
  <p class="abs url url--back">http://www.halcyon-networks.net</p>
</section>

</body>
</html>
```